Harbor Networks Pty Ltd

We are a Sydney based IT services company, providing managed services for corporate clients, established for over 10 years. Amongst our services we provide full infrastructure support, maintenance and upgrades. We also provide helpdesk/remote support and cloud services.

We were hoping to keep our original colours and our logo (Blue and Green, please visit our website www.harbornetworks-demo.com.au) however we are looking for a new business card design (with better resolution and finish) with multiple variation of the blue and green colour design options. Happy for alternative suggestion. ie new blue and green / grey and green / blue and grey et and please feel free to update current logo size ie large or smaller. (Attached our current logo and business card desig)

Business

Contact Information for Business Card

Name, Title, Address, Contract Information, Company Name and Logo.
(QR code if possible)

Colors
0455a3
33a6d7
3276b5
85acd3
85cae6
9bcb3c
add136
cadf82
e9f1ce

```html
<!DOCTYPE html>
<html lang="en">
<head>
<meta charset="utf-8">
<title>Harbor Networks – Business Card</title>
<link href="https://fonts.googleapis.com/css2?family=Open+Sans:wght@400;700&display=swap" rel="stylesheet">
<style>
  :root {
    --brand-blue: #0455a3;
    --card-blue: #1670a8;
    --brand-green: #76bc43;
    --ink-white: #ffffff;
    --card-border: #2a2a2a;
    --page-bg: #ffffff;
    --pattern-light: rgba(133, 172, 211, 0.35);
    --pattern-fade: rgba(133, 172, 211, 0);
  }
  * { box-sizing: border-box; }
  html, body {
    margin: 0;
    width: 1200px;
    height: 1000px;
    overflow: hidden;
    background: var(--page-bg);
    font-family: "Open Sans", Verdana, sans-serif;
  }
  .canvas { position: relative; width: 1200px; height: 1000px; }

  .card { position: absolute; width: 462px; height: 804px; }

  /* Front */
  .card--front {
    left: 116px; top: 101px;
    background: var(--page-bg);
    border: 1.5px solid var(--card-border);
  }
  .front-brand {
    position: absolute;
    left: 0; right: 0; top: 455px;
    display: flex; align-items: center; justify-content: center; gap: 12px;
  }
  .front-brand__square {
    width: 30px; height: 30px;
    background: var(--brand-green);
  }
  .front-brand__name {
    font-size: 40px; font-weight: 700;
    color: var(--brand-blue);
    letter-spacing: -0.5px;
  }

  /* Back */
  .card--back {
    left: 618px; top: 99px;
    background: var(--card-blue);
    border: 1.5px solid var(--card-border);
    color: var(--ink-white);
    overflow: hidden;
  }
  .back-pattern {
    position: absolute;
    left: 0; top: 545px; width: 400px; height: 259px;
    background: radial-gradient(ellipse at 50% 40%, var(--pattern-light), var(--pattern-fade) 70%);
  }
  .back-brand {
    position: absolute; left: 0; right: 0; top: 140px;
    text-align: center;
    font-size: 30px; font-weight: 700;
    color: var(--brand-green);
  }
  .person-name {
    position: absolute; left: 0; right: 0; top: 256px;
    text-align: center;
    font-size: 38px; font-weight: 700; margin: 0;
  }
  .person-title {
    position: absolute; left: 0; right: 0; top: 312px;
    text-align: center;
    font-size: 25px; margin: 0;
  }
  .person-title__dot {
    display: inline-block; width: 10px; height: 10px;
    border: 2px solid var(--ink-white);
    vertical-align: middle; margin: 0 3px 4px;
  }
  .contact-row {
    position: absolute;
    display: flex; align-items: center;
    font-size: 18px; white-space: nowrap;
  }
  .contact-row svg { width: 16px; height: 16px; fill: var(--ink-white); flex: none; }
  .contact-row--phones { left: 30px; }
  .phone-item { display: flex; align-items: center; gap: 6px; }
  .phone-item--right { position: absolute; left: 212px; }
  .phone-item__d { font-weight: 700; }
  .web-list { position: absolute; left: 72px; top: 486px; }
  .web-list .contact-row { position: static; gap: 12px; height: 30px; font-size: 17px; }
  .web-list__at { width: 16px; text-align: center; font-weight: 700; }
  .address {
    position: absolute; left: 74px; top: 616px;
    font-size: 18px; line-height: 26px;
  }
  .address__line { display: flex; align-items: center; gap: 4px; }
  .address__line--indent { padding-left: 20px; }
  .address svg { width: 16px; height: 20px; fill: var(--ink-white); }
</style>
</head>
<body>
<main class="canvas">

  <section class="card card--front" aria-label="Card front">
    <div class="front-brand">
      <span class="front-brand__square"></span>
      <span class="front-brand__name">harbornetworks</span>
    </div>
  </section>

  <section class="card card--back" aria-label="Card back">
    <div class="back-pattern" role="img" aria-label="Faint background pattern of overlapping outlined squares"></div>

    <div class="back-brand">Harbor Networks</div>

    <h1 class="person-name">Tom Keller</h1>
    <p class="person-title">Director<span class="person-title__dot"></span>Managed IT Services</p>

    <div class="contact-row contact-row--phones" style="top:388px;">
      <span class="phone-item">
        <svg viewBox="0 0 16 16"><path d="M3 1l3 3-1.5 2c1 2 2.5 3.5 4.5 4.5L11 9l3 3-2 2.5C6 14 2 10 1.5 3z"/></svg>
        <span style="margin-left:42px;">1300 555 019</span>
      </span>
      <span class="phone-item phone-item--right"><span class="phone-item__d">D</span>+ 61 2 5550 1234</span>
    </div>

    <div class="contact-row contact-row--phones" style="top:426px;">
      <span class="phone-item">
        <svg viewBox="0 0 16 16"><path d="M4 0h8a1 1 0 0 1 1 1v14a1 1 0 0 1-1 1H4a1 1 0 0 1-1-1V1a1 1 0 0 1 1-1zm1 2v10h6V2zm3 11a1 1 0 1 0 0 2 1 1 0 0 0 0-2z"/></svg>
        <span style="margin-left:4px;">+ 61 400 555 123</span>
      </span>
      <span class="phone-item phone-item--right">
        <svg viewBox="0 0 16 16"><path d="M4 1h6v5H4zM1 7h14v6H1zm2 2v2h10V9zM3 14h10v1H3z"/></svg>
        + 61 2 5550 9876
      </span>
    </div>

    <div class="web-list">
      <div class="contact-row">
        <svg viewBox="0 0 16 16"><path d="M8 1a6 6 0 0 0-6 6v4h3V7H3.5a4.5 4.5 0 0 1 9 0H11v4h2v1h-3v1.5h4V7a6 6 0 0 0-6-6z"/></svg>
        <span>support@harbornetworks-demo.com.au</span>
      </div>
      <div class="contact-row">
        <span class="web-list__at">@</span>
        <span>tom.keller@harbornetworks-demo.com.au</span>
      </div>
      <div class="contact-row">
        <svg viewBox="0 0 16 16"><path d="M8 1a7 7 0 1 0 0 14A7 7 0 0 0 8 1zm-1 2.2V6H4.3A5 5 0 0 1 7 3.2zm2 0A5 5 0 0 1 11.7 6H9zM3.1 7.5H7v1H3.1zm5.9 0h3.9v1H9zM4.3 10H7v2.8A5 5 0 0 1 4.3 10zM9 10h2.7A5 5 0 0 1 9 12.8z"/></svg>
        <span>www.harbornetworks-demo.com.au</span>
      </div>
    </div>

    <div class="address">
      <div class="address__line">
        <svg viewBox="0 0 16 20"><path d="M8 0a7 7 0 0 0-7 7c0 5 7 13 7 13s7-8 7-13a7 7 0 0 0-7-7zm0 4a3 3 0 1 1 0 6 3 3 0 0 1 0-6z"/></svg>
        <span>Harbor Networks Pty Ltd</span>
      </div>
      <div class="address__line address__line--indent">Level 4, 18 Example Street</div>
      <div class="address__line address__line--indent">Sydney NSW 2000 Australlia</div>
    </div>
  </section>

</main>
</body>
</html>
```